Brightmere Business Card Redesign & Logo Update

We need to update our business cards to something more modern and fresh. Brightmere can provide the current color schemes and old design examples, but welcome creativity in helping us with this redesign. PLEASE NOTE that we no longer utilize the "tree" and/or "leaf" imagery in our branding. If able would apprecaite an update on the quality of our "words only" logo in Ai. / PNG formats too.

Target Market(s)

Investors, landowners, corporate partners, contractors

Industry/Entity Type

Environmental Restoration & Conservation

Contact Information for Business Card

Logo, persons name, title, mailing address, phone and email, website url

Font styles to use
Other font styles liked:
• Merriweather

Requirements
Nice to have
• Logo, persons name, title, mailing address, phone and email, website url, but open to ideams
Should not have
• No all back backgrounds

```html
<!DOCTYPE html>
<html lang="en">
<head>
<meta charset="UTF-8">
<title>Brightmere Business Cards</title>
<link href="https://fonts.googleapis.com/css2?family=Bebas+Neue&family=Open+Sans:wght@400;600;700&display=swap" rel="stylesheet">
<style>
  :root {
    --backdrop: #e9eaec;
    --card: #ffffff;
    --orange: #ee7f23;
    --orange-name: #f0612b;
    --green: #137f3f;
    --ink: #1a1a1a;
    --text: #333333;
  }
  * { box-sizing: border-box; margin: 0; padding: 0; }
  html, body {
    width: 1200px; height: 780px; overflow: hidden;
    background: var(--backdrop);
  }
  .canvas { position: relative; width: 1200px; height: 780px; }
  .card {
    position: absolute; width: 560px; height: 320px;
    background: var(--card); border-radius: 22px; overflow: hidden;
    box-shadow: 0 8px 24px rgba(0,0,0,.18);
  }
  .card--front { left: 60px; top: 50px; }
  .card--back { left: 580px; top: 410px; }
  .card__bands { position: absolute; inset: 0; width: 100%; height: 100%; }
  .brand { position: absolute; text-align: center; }
  .brand__name {
    font-family: 'Bebas Neue', sans-serif; color: var(--green);
    line-height: .86; letter-spacing: 1px; display: block;
  }
  .brand__tagline {
    font-family: 'Bebas Neue', sans-serif; color: var(--ink);
    letter-spacing: .5px; display: block;
  }
  .card--front .brand { left: 0; right: 0; top: 62px; }
  .card--front .brand__name { font-size: 132px; }
  .card--front .brand__tagline { font-size: 34px; margin-top: 2px; }
  .card--back .brand { left: 0; right: 0; top: 34px; }
  .card--back .brand__name { font-size: 78px; }
  .card--back .brand__tagline { font-size: 21px; margin-top: 1px; }
  .person { position: absolute; left: 90px; top: 182px; width: 190px; text-align: right; font-family: 'Open Sans', sans-serif; }
  .person__name { font-size: 25px; font-weight: 700; color: var(--orange-name); white-space: nowrap; }
  .person__title { font-size: 15px; color: var(--text); margin-top: 2px; }
  .divider { position: absolute; left: 300px; top: 160px; width: 1px; height: 76px; background: var(--ink); }
  .contacts { position: absolute; left: 322px; top: 150px; list-style: none; font-family: 'Open Sans', sans-serif; font-size: 13.5px; color: var(--text); }
  .contacts li { display: flex; align-items: center; gap: 8px; height: 24px; }
  .contacts svg { width: 14px; height: 14px; flex: none; fill: var(--orange-name); }
</style>
</head>
<body>
<div class="canvas">
  <section class="card card--front">
    <svg class="card__bands" viewBox="0 0 560 320" aria-hidden="true">
      <polygon points="0,300 318,300 336,320 0,320" fill="var(--orange)"/>
      <polygon points="300,272 560,272 560,294 322,294" fill="var(--green)"/>
    </svg>
    <div class="brand">
      <span class="brand__name">Brightmere</span>
      <span class="brand__tagline">Environmental Credit Company</span>
    </div>
  </section>

  <section class="card card--back">
    <svg class="card__bands" viewBox="0 0 560 320" aria-hidden="true">
      <polygon points="0,300 318,300 336,320 0,320" fill="var(--orange)"/>
      <polygon points="300,272 560,272 560,294 322,294" fill="var(--green)"/>
    </svg>
    <div class="brand">
      <span class="brand__name">Brightmere</span>
      <span class="brand__tagline">Environmental Credit Company</span>
    </div>
    <div class="person">
      <p class="person__name">Lenka Horakova</p>
      <p class="person__title">Managing Director</p>
    </div>
    <div class="divider"></div>
    <ul class="contacts">
      <li>
        <svg viewBox="0 0 24 24"><path d="M6.6 10.8a15.1 15.1 0 0 0 6.6 6.6l2.2-2.2a1 1 0 0 1 1-.25 11.4 11.4 0 0 0 3.6.57 1 1 0 0 1 1 1V20a1 1 0 0 1-1 1A17 17 0 0 1 3 4a1 1 0 0 1 1-1h3.5a1 1 0 0 1 1 1c0 1.25.2 2.45.57 3.57a1 1 0 0 1-.25 1z"/></svg>
        (555) 014-2290
      </li>
      <li>
        <svg viewBox="0 0 24 24"><path d="M2 5h20v14H2zm2 2v.5l8 5 8-5V7zm0 2.8V17h16V9.8l-8 5z"/></svg>
        info@brightmere-credit.com
      </li>
      <li>
        <svg viewBox="0 0 24 24"><path d="M12 2a10 10 0 1 0 0 20 10 10 0 0 0 0-20zm6.9 6h-3a15.6 15.6 0 0 0-1.4-3.6A8 8 0 0 1 18.9 8zM12 4a14 14 0 0 1 1.9 4h-3.8A14 14 0 0 1 12 4zM4.3 14a8 8 0 0 1 0-4h3.4a16 16 0 0 0 0 4zm.8 2h3a15.6 15.6 0 0 0 1.4 3.6A8 8 0 0 1 5.1 16zm3-8h-3a8 8 0 0 1 4.4-3.6A15.6 15.6 0 0 0 8.1 8zM12 20a14 14 0 0 1-1.9-4h3.8A14 14 0 0 1 12 20zm2.3-6H9.7a14.7 14.7 0 0 1 0-4h4.6a14.7 14.7 0 0 1 0 4zm.2 5.6a15.6 15.6 0 0 0 1.4-3.6h3a8 8 0 0 1-4.4 3.6zm1.8-5.6a16 16 0 0 0 0-4h3.4a8 8 0 0 1 0 4z"/></svg>
        www.brightmere-credit.com
      </li>
    </ul>
  </section>
</div>
</body>
</html>
```